Keelrock Data Partners (KDP) Business Card Design

I would like to create double-sided business cards that contain:
1) Name: Marcus Tolliver
2) Phone Number: +1 (555) 018-2947
3) Email: Marcus.Tolliver@KeelrockDataPartners.com
4) Website: KeelrockDataPartners.com

I would like to include my logo and a color scheme similar to the Vantorra Grand Prix Kelvex team color scheme (black, silver, greenish-blue – but can also include regular blue)

Logos attached.

What we do: Our company develops and delivers innovative and pragmatic information technology and cybersecurity risk and compliance solutions for organizations in the commercial market as well as the federal, and state/local sectors.

```html
<!DOCTYPE html>
<html lang="en">
<head>
<meta charset="utf-8">
<title>Keelrock Data Partners – Business Card</title>
<link href="https://fonts.googleapis.com/css2?family=Arimo:wght@400;700&display=swap" rel="stylesheet">
<style>
  :root {
    --backdrop: #3b3c3f;
    --card-white: #f4f4f2;
    --brand-blue: #0a67b0;
    --brand-blue-deep: #0b4f92;
    --brand-teal: #1bb3ac;
    --edge-teal: #0f8f86;
    --ink: #2f3134;
    --ink-soft: #6e7176;
    --on-blue: #eef4fa;
  }
  * { box-sizing: border-box; margin: 0; padding: 0; }
  html, body { width: 1200px; height: 1108px; overflow: hidden; }
  body {
    background: var(--backdrop);
    font-family: "Arimo", Arial, sans-serif;
    display: flex;
    flex-direction: column;
    align-items: center;
    justify-content: center;
    gap: 48px;
  }
  .card {
    width: 840px;
    height: 480px;
    border-bottom: 6px solid var(--edge-teal);
    position: relative;
  }
  /* Front side */
  .card-front { background: var(--card-white); }
  .front-mark {
    position: absolute;
    top: 40px;
    right: 44px;
    display: flex;
    align-items: center;
    gap: 10px;
    font-weight: 700;
    font-size: 30px;
    color: var(--brand-blue-deep);
    letter-spacing: 1px;
  }
  .front-mark .dot {
    width: 22px; height: 22px; border-radius: 50%;
    background: var(--brand-teal);
  }
  .contact-block {
    position: absolute;
    top: 120px;
    left: 0; right: 0;
    text-align: center;
    color: var(--ink);
  }
  .person-name {
    font-size: 40px;
    font-weight: 700;
    color: var(--brand-blue-deep);
  }
  .person-title {
    font-size: 20px;
    color: var(--ink-soft);
    margin-top: 6px;
  }
  .contact-icons {
    display: flex;
    justify-content: center;
    gap: 18px;
    margin: 18px 0 14px;
  }
  .contact-icons svg { width: 20px; height: 20px; fill: var(--brand-teal); }
  .contact-line { font-size: 23px; line-height: 1.38; }
  /* Back side */
  .card-back {
    background: linear-gradient(160deg, #0f77c0 0%, var(--brand-blue) 55%, #0860a6 100%);
    display: flex;
    align-items: center;
    justify-content: center;
  }
  .back-mark {
    display: flex;
    align-items: center;
    gap: 26px;
    color: var(--on-blue);
  }
  .back-mark .dot {
    width: 90px; height: 90px; border-radius: 50%;
    background: var(--on-blue);
  }
  .back-mark .divider {
    width: 2px; height: 150px; background: var(--on-blue); opacity: .8;
  }
  .back-mark .wordmark {
    font-size: 54px;
    line-height: 1.02;
    letter-spacing: 4px;
    text-transform: uppercase;
    font-weight: 400;
  }
</style>
</head>
<body>
  <section class="card card-front" aria-label="Business card front">
    <div class="front-mark"><span class="dot"></span>KDP</div>
    <div class="contact-block">
      <h1 class="person-name">Marcus Tolliver</h1>
      <p class="person-title">President</p>
      <div class="contact-icons">
        <svg viewBox="0 0 24 24" aria-label="Phone"><path d="M6.6 10.8a15.1 15.1 0 0 0 6.6 6.6l2.2-2.2a1 1 0 0 1 1-.25 11.4 11.4 0 0 0 3.6.57 1 1 0 0 1 1 1V20a1 1 0 0 1-1 1A17 17 0 0 1 3 4a1 1 0 0 1 1-1h3.5a1 1 0 0 1 1 1c0 1.25.2 2.45.57 3.57a1 1 0 0 1-.25 1z"/></svg>
        <svg viewBox="0 0 24 24" aria-label="Email"><path d="M2 5h20v14H2z M3.5 6.5 12 13l8.5-6.5" fill="var(--brand-teal)" stroke="var(--card-white)" stroke-width="1.4"/></svg>
        <svg viewBox="0 0 24 24" aria-label="Website"><circle cx="12" cy="12" r="10"/><path d="M2 12h20M12 2c3 3 3 17 0 20M12 2c-3 3-3 17 0 20" fill="none" stroke="var(--card-white)" stroke-width="1.3"/></svg>
      </div>
      <p class="contact-line">+1 (555) 018-2947</p>
      <p class="contact-line">Marcus.Tolliver@KeelrockDataPartners.com</p>
      <p class="contact-line">www.KeelrockDataPartners.com</p>
      <p class="contact-line">4120 Larkspur Way, Halden, Canada 58210</p>
    </div>
  </section>

  <section class="card card-back" aria-label="Business card back">
    <div class="back-mark">
      <span class="dot"></span>
      <span class="divider"></span>
      <p class="wordmark">Keelrock<br>Data<br>Partners</p>
    </div>
  </section>
</body>
</html>
```